Poster Design for Film: 'Tres Lunas'

Tres Lunas means "two times" in Spanish. This short film is based on the true story of Cuban refugee during the take over of the Ordaz regime in 1959 and how is experiences and stories affected his children and grandchildren. Tres Lunas tells the story of Daniel- a recent grad who is forced to choose between his critically ill grandfather, the business opportunity of a lifetime, and maintaining a relationship with his love interest, Margaret. Through his grandfather's recollections as a young man in 1950's Cuba, Daniel gains a new outlook on life and the things that matter most.

This poster should evoke the drama and truth that the film approaches in a cinematic manner while maintaining the influences of true Cuban culture and history as perceived by a Miami audience today.

For more information please take a look at our fund raising site:
http://www.fundhaven.example/projects/tres-lunas

The grandfather's current life (the Cuban revolutionary/refugee as an old man):
www.clipvault.example/41592867
password: treslunas

A quick teaser of the film, exploring the lives of Daniel (the protagonist; grandson to Cuban refugee/revolutionary) and Meg (Daniel's love interest he neglects to commit to):

http://www.streamtube.example/watch?v=QbRtPwXnLeK

Please let me know if you would like any stills of the film, have any questions, etc. Thanks!

Hey all! So sorry for the delay on the stills- we had some serious technical issues, but now they are up!

Please let me know if you have any questions. We'll be uploaded more stills to choose from tonight.

Thanks!

Hey all!
Unless you need something in specific, I have just uploaded the final stills for the poster. Feel free to use any of the images, but please keep in mind that the main characters are Dan (the grandson), and his grandfather Arturo both young and old. In other words- the three guys.

Please let me know if you have any questions. Thanks! 

Here are some small text details for the bottom of the poster:

A Copper Lantern Production in association with BrightKiln Studios and the Coastal Pines University. Starring Brett Solano, Celina Fuentes, Omar Bustillo, Lucia Ortega, Farid Khoury. Written, Directed, & Produced by Marcos Ibarra. Director of Photography Tomas Varela. Edited by Marcos Ibarra & Tomas Varela.

Hey designers!

I've just uploaded a new still of the main character. Please try to include it in your design, as it is preferred over the other stills of the main character.

Thanks!

I've just uploaded two small logos to be featured on the bottom of the poster.

Thanks!

Target Market(s)

Hollywood. Cuban-Americans. Miamians. Film Critics. Students. Professors.

Adults based in Los Angeles and Miami aged 21-50 that speak English and Spanish and are in the art and entertainment industry.

Industry/Entity Type

Business

Requirements
Must have
• Must evoke the style of Cuba in the late 1950's while staying true to current day culture/style for 20-somethings in America (specifically LA, NYC, Miami).
Nice to have
• A sort of serious, almost stoic style that could possibly evoke a melancholic reaction.
Should not have
• Anything that evokes a daytime soap opera.

```html
<!DOCTYPE html>
<html lang="en">
<head>
<meta charset="utf-8">
<title>Tres Lunas — Film Poster</title>
<link rel="stylesheet" href="https://fonts.googleapis.com/css2?family=Russo+One&family=Ubuntu:wght@500&display=swap">
<style>
  :root {
    --flag-blue: #2a5a9a;
    --flag-white: #f4f1ea;
    --flag-red: #e4550f;
    --title-white: #ffffff;
    --title-orange: #f05a0a;
    --tagline-ink: #14213a;
    --photo-light: #e9e9e9;
    --photo-mid: #8a8a8a;
    --photo-dark: #1c1c1c;
  }
  * { margin: 0; padding: 0; box-sizing: border-box; }
  html, body { width: 800px; height: 1200px; overflow: hidden; background: #ffffff; }
  .poster { position: relative; width: 800px; height: 1200px; overflow: hidden; }

  .still {
    position: absolute; left: 0; top: 0; width: 800px; height: 705px;
    background:
      radial-gradient(ellipse 260px 340px at 150px 420px, var(--photo-dark) 0%, rgba(28,28,28,0.85) 55%, rgba(28,28,28,0) 100%),
      radial-gradient(ellipse 230px 300px at 520px 330px, #5e5e5e 0%, rgba(120,120,120,0.6) 60%, rgba(120,120,120,0) 100%),
      linear-gradient(90deg, var(--photo-mid) 0%, var(--photo-light) 45%, var(--photo-light) 100%);
  }

  .flag { position: absolute; left: 0; top: 700px; width: 800px; height: 500px; display: block; }

  .title {
    position: absolute; left: 0; top: 628px; width: 800px; height: 140px;
    display: flex; justify-content: center; align-items: center; gap: 72px;
    font-family: "Russo One", "Arial Black", sans-serif; font-weight: 400;
    font-size: 124px; line-height: 140px; letter-spacing: 0;
    white-space: nowrap;
    transform: scale(0.8, 1.05); transform-origin: 50% 50%;
    text-shadow: 6px 8px 10px rgba(0,0,0,0.55);
  }
  .title-word--first { color: var(--title-white); }
  .title-word--second { color: var(--title-orange); }

  .tagline {
    position: absolute; left: 271px; top: 776px;
    font-family: "Ubuntu", "Helvetica", sans-serif; font-weight: 500;
    font-size: 22px; letter-spacing: 0.3px; color: var(--tagline-ink);
    white-space: nowrap;
  }
</style>
</head>
<body>
<main class="poster">
  <div class="still" role="img" aria-label="Black and white still: a young woman with long dark hair holds the face of a young mustached man behind prison bars, foreheads nearly touching"></div>

  <svg class="flag" viewBox="0 0 800 500" aria-hidden="true">
    <defs>
      <linearGradient id="flag-wear" x1="0" y1="0" x2="1" y2="1">
        <stop offset="0" stop-color="#000" stop-opacity="0.08"/>
        <stop offset="0.5" stop-color="#fff" stop-opacity="0"/>
        <stop offset="1" stop-color="#000" stop-opacity="0.1"/>
      </linearGradient>
    </defs>
    <rect class="stripe-blue" x="0" y="0" width="800" height="162" fill="var(--flag-blue)"/>
    <rect class="stripe-white" x="0" y="162" width="800" height="166" fill="var(--flag-white)"/>
    <rect class="stripe-blue" x="0" y="328" width="800" height="172" fill="var(--flag-blue)"/>
    <polygon class="flag-triangle" points="0,5 556,250 0,500" fill="var(--flag-red)"/>
    <polygon class="flag-star" fill="var(--flag-white)"
      points="176,292 199,362 272,362 213,405 236,475 176,432 116,475 139,405 80,362 153,362"/>
    <rect x="0" y="0" width="800" height="500" fill="url(#flag-wear)"/>
  </svg>

  <h1 class="title">
    <span class="title-word title-word--first">TRES</span>
    <span class="title-word title-word--second">LUNAS</span>
  </h1>
  <p class="tagline">BASED ON TRUE EVENTS</p>
</main>
</body>
</html>
```